Maple Hollow Bloom Panels Business card

Looking to have a business card design incorporating my logo for my flower wall business.

Industry/Entity Type

Wedding & event planning

Contact Information for Business Card

My business logo, my name - Lena Whitcombe (owner), my tagline - We add the bloom to your day, phone # 401-726-3148, email address - maplehollowbloompanels@mailvane.net, my website - maplehollowbloompanels.net, Instagram handle- @maplehollowbloompanels, FB handle Handle - maplehollowbloompanels

Font styles to use
Other font styles liked:
• Sentaina is the font that is used in my logo

Requirements
Must have
• Would like a double sided business card

```html
<!DOCTYPE html>
<html lang="en">
<head>
<meta charset="utf-8">
<title>Maple Hollow Bloom Panels — Business Card</title>
<link rel="stylesheet" href="https://fonts.googleapis.com/css2?family=Jost:wght@300;400;500;600&family=Mrs+Saint+Delafield&display=swap">
<style>
  :root {
    --page: #f6f6f4;
    --magenta: #e2339b;
    --card-white: #f3f3f3;
    --ink: #262626;
  }
  * { box-sizing: border-box; margin: 0; padding: 0; }
  html, body { width: 1199px; height: 1200px; overflow: hidden; background: var(--page); }
  body { position: relative; font-family: "Jost", sans-serif; }

  .card {
    position: absolute;
    left: 150px;
    width: 900px;
    height: 551px;
    box-shadow: 8px 9px 10px rgba(0,0,0,.45);
    overflow: hidden;
  }

  /* Front */
  .card--front {
    top: 24px;
    background:
      radial-gradient(ellipse 200px 150px at 120px 110px, rgba(180,20,110,.35), transparent 70%),
      radial-gradient(ellipse 160px 120px at 100px 330px, rgba(180,20,110,.3), transparent 70%),
      radial-gradient(ellipse 220px 160px at 700px 430px, rgba(180,20,110,.25), transparent 70%),
      radial-gradient(ellipse 180px 120px at 330px 70px, rgba(200,40,130,.25), transparent 70%),
      var(--magenta);
  }
  .brand-seal {
    position: absolute;
    left: 283px; top: 92px;
    width: 334px; height: 334px;
    border-radius: 50%;
    background: #fff;
    display: flex; align-items: center; justify-content: center;
    text-align: center;
  }
  .brand-name {
    font-weight: 500;
    font-size: 32px;
    line-height: 1.25;
    letter-spacing: .04em;
    color: var(--ink);
  }
  .tagline {
    position: absolute;
    left: 0; right: 0; top: 466px;
    text-align: center;
    color: #fff;
    font-weight: 400;
    font-size: 23px;
    letter-spacing: .32em;
  }

  /* Back */
  .card--back {
    top: 625px;
    background: var(--card-white);
  }
  .bloom-art {
    position: absolute;
    right: 0; top: 0;
    width: 195px; height: 280px;
    border-radius: 0 0 0 60%;
    background: radial-gradient(circle at 70% 35%, rgba(224,140,192,.45), rgba(224,140,192,.15) 70%, transparent 100%);
  }
  .holder-name {
    position: absolute;
    left: 0; right: 0; top: 128px;
    text-align: center;
    font-family: "Mrs Saint Delafield", cursive;
    font-weight: 400;
    font-size: 84px;
    line-height: 1;
    color: var(--magenta);
  }
  .holder-role {
    position: absolute;
    left: 0; right: 0; top: 232px;
    text-align: center;
    font-weight: 600;
    font-size: 28px;
    letter-spacing: .2em;
    color: var(--magenta);
  }
  .contact-list {
    position: absolute;
    left: 0; right: 0; top: 314px;
    list-style: none;
    text-align: center;
    color: var(--magenta);
    font-size: 23px;
    font-weight: 400;
  }
  .contact-list li { height: 34px; display: flex; align-items: center; justify-content: center; gap: 10px; }
  .icon { width: 24px; height: 24px; flex: none; }
  .divider {
    position: absolute;
    left: 240px; width: 426px; top: 436px;
    height: 2px; background: var(--magenta);
  }
  .social {
    position: absolute;
    top: 456px;
    display: flex; align-items: center; gap: 10px;
    color: var(--magenta);
    font-size: 21px;
  }
  .social--insta { left: 146px; }
  .social--fb { left: 486px; }
  .social-dot { width: 24px; height: 24px; border-radius: 50%; background: var(--magenta); flex: none; }
</style>
</head>
<body>

<section class="card card--front" aria-label="Card front">
  <div class="brand-seal">
    <p class="brand-name">Maple Hollow<br>Bloom Panels</p>
  </div>
  <p class="tagline">WE ADD THE BLOOM TO YOUR DAY</p>
</section>

<section class="card card--back" aria-label="Card back">
  <div class="bloom-art" role="img" aria-label="Line-drawn pink peony with gold seed dots in the top corner"></div>

  <h1 class="holder-name">Lena Whitcombe</h1>
  <p class="holder-role">OWNER</p>

  <ul class="contact-list">
    <li>
      <svg class="icon" viewBox="0 0 24 24" aria-hidden="true"><circle cx="12" cy="12" r="12" fill="var(--magenta)"/><path d="M8.2 6.5l2 .1 1 2.6-1.3 1c.7 1.5 1.8 2.6 3.3 3.3l1-1.3 2.6 1 .1 2c-.2.8-1 1.3-1.8 1.2C10 16 7.9 13.9 7.4 8.3c-.1-.8.4-1.6.8-1.8z" fill="#fff"/></svg>
      <span>401-726-3148</span>
    </li>
    <li>
      <svg class="icon" viewBox="0 0 24 24" aria-hidden="true"><circle cx="12" cy="12" r="12" fill="var(--magenta)"/><rect x="6.5" y="8" width="11" height="8" rx="1" fill="none" stroke="#fff" stroke-width="1.4"/><path d="M6.8 8.5L12 12.6l5.2-4.1" fill="none" stroke="#fff" stroke-width="1.4"/></svg>
      <span>maplehollowbloompanels@mailvane.net</span>
    </li>
    <li>
      <svg class="icon" viewBox="0 0 24 24" aria-hidden="true"><circle cx="12" cy="12" r="12" fill="var(--magenta)"/><g fill="none" stroke="#fff" stroke-width="1.3"><circle cx="12" cy="12" r="6"/><ellipse cx="12" cy="12" rx="2.6" ry="6"/><path d="M6 12h12M7 9h10M7 15h10"/></g></svg>
      <span>maplehollowbloompanels.net</span>
    </li>
  </ul>

  <div class="divider"></div>

  <p class="social social--insta"><span class="social-dot"></span><span>@maplehollowbloompanels</span></p>
  <p class="social social--fb"><span class="social-dot"></span><span>maplehollowbloompanels</span></p>
</section>

</body>
</html>
```